Modern design for a Septic Tank maintenance company

Task Description
- The design should be based around the attached HPID (home page information design) called Tane Drain Septic Services HPID. The table boxes are just for approximate placement of information – you DON'T have to make it look exactly like this.
- Information only is in orange text. Copy to go on the design in black text. Some instructions are in the HPID. Please be creative! You don’t have to use the exact images provided if you have a better idea.

- The design needs to be clean and spacious. Please use the colours from the logos in the website design. LOTS of white too. Don't need to use all the images attached some are customer supplied and might only be good for the smaller images.

I've attached home page gallery example photo called Piha beach. You can use this or something similar - be creative please!

Width of content will be 1100 pixels when implemented as a web page. Header height (without nav bar) 150-160 pixels.

The winning PSD file will have to be provided as follows…
1. Canvas size of 2000px x 2000px - 72ppi in Adobe Photoshop (CS5 compatible)
2. Width of content section is 1100px wide - centered in the canvas
3. Any button rollovers/hovers in the PSD as hidden layers.
4. All fonts used must be Google fonts (except for the fonts in the header at the top of the page).
5. You will need to supply the chosen home page plus one example page (example page as a style guide for how all other pages will look). Example page is only the header and navigational bar at the top, an empty sector in the middle with a column (180 px wide) which can be left or right aligned which means the main sector is 920 pixels wide, and then the footer at the bottom of the page.

```html
<!DOCTYPE html>
<html lang="en">
<head>
<meta charset="utf-8">
<title>Tane Drain Septic Services</title>
<link href="https://fonts.googleapis.com/css2?family=Open+Sans:wght@400;600;700;800&display=swap" rel="stylesheet">
<style>
:root{
  --teal:#19a596;
  --teal-dark:#12877a;
  --nav:#3d3d3d;
  --nav-active:#262626;
  --ink:#333;
  --muted:#7a7a7a;
  --line:#d6d6d6;
  --footer:#2c2c2c;
  --footer-bottom:#1f1f1f;
  --white:#fff;
}
*{box-sizing:border-box;margin:0;padding:0}
html,body{width:753px;height:1200px;overflow:hidden;background:var(--white)}
body{font-family:"Open Sans",Arial,sans-serif;color:var(--ink);position:relative}
.wrap{position:absolute;left:25px;width:703px}

/* header */
.site-header{position:absolute;top:0;left:0;width:753px;height:36px}
.brand{position:absolute;left:25px;top:8px;display:flex;align-items:center;gap:6px}
.brand-dot{width:18px;height:18px;border-radius:50%;background:var(--teal)}
.brand-name{font-size:11px;font-weight:800;color:var(--teal);line-height:1}
.tagline{position:absolute;left:270px;top:6px;width:208px;font-size:5.5px;line-height:8px;color:var(--muted);text-align:center}
.contact{position:absolute;right:25px;top:2px;text-align:right;line-height:1.05}
.contact .service{font-size:5.5px;color:var(--muted)}
.contact .area{font-size:7px;font-weight:700;color:var(--ink)}
.contact .phone{font-size:8px;font-weight:700;color:var(--teal)}

/* nav */
.main-nav{position:absolute;top:37px;left:25px;width:703px;height:15px;background:var(--nav);display:flex}
.main-nav a{font-size:5.5px;font-weight:700;color:var(--white);text-decoration:none;padding:0 11px;line-height:15px;letter-spacing:.2px}
.main-nav a.active{background:var(--nav-active)}

/* hero */
.hero{position:absolute;top:52px;left:0;width:753px;height:378px;background:linear-gradient(180deg,#9cc4dc 0%,#c8dde6 38%,#5e8f86 60%,#3a6a5a 80%,#b9ad94 100%)}
.hero-box{position:absolute;left:25px;top:165px;width:165px;background:rgba(25,70,70,.78);padding:7px 8px}
.hero-box h1{font-size:8.5px;font-weight:800;color:var(--white);line-height:11px}
.hero-box p{font-size:4.8px;color:#dfeeee;line-height:7px;margin-top:4px}
.hero-btn{position:absolute;left:25px;top:248px;background:var(--teal);color:var(--white);font-size:6.5px;font-weight:700;padding:4px 8px}
.hero-arrow{position:absolute;top:200px;width:14px;height:24px;background:rgba(40,40,40,.55)}
.hero-arrow.left{left:0}.hero-arrow.right{right:0}

/* feature columns */
.features{position:absolute;top:448px;left:66px;width:606px;display:flex;justify-content:space-between}
.feature{width:180px;text-align:center}
.feature h2{font-size:8px;font-weight:800;color:var(--teal);line-height:10.5px;height:36px;text-transform:uppercase}
.feature-img{width:180px;height:90px;background:linear-gradient(160deg,#8fb07c,#5d7f53 60%,#9a9c86)}
.feature p{font-size:5.3px;line-height:8.6px;color:var(--muted);margin:10px 2px 0}
.more{display:inline-block;margin-top:8px;background:var(--nav);color:var(--white);font-size:5px;font-weight:700;padding:4px 8px}

/* quote */
.quote{top:760px;text-align:center}
.quote h2{font-size:22px;font-weight:600;color:var(--teal);line-height:26px}
.quote .sub{font-size:7px;color:var(--muted);margin-top:2px}
.quote-row{display:flex;gap:12px;margin-top:14px}
.field{flex:1;height:18px;border:1px solid var(--line);font-size:6px;color:var(--muted);text-align:left;padding:5px 6px}
.field.details{height:45px;margin-top:10px}
.submit{display:inline-block;margin-top:12px;background:var(--teal);color:var(--white);font-size:6.5px;font-weight:700;padding:5px 10px}

/* footer */
.site-footer{position:absolute;top:952px;left:0;width:753px;height:214px;background:var(--footer)}
.foot-links{position:absolute;left:100px;top:30px;list-style:none}
.foot-links li{font-size:6.5px;color:#ddd;line-height:14px;display:flex;align-items:center;gap:5px}
.foot-links li::before{content:"";width:0;height:0;border-left:4px solid var(--teal);border-top:3px solid transparent;border-bottom:3px solid transparent}
.foot-col{position:absolute;top:28px}
.foot-col h3{font-size:7.5px;font-weight:700;color:var(--teal);margin-bottom:5px}
.foot-col p{font-size:5.3px;line-height:8px;color:#bdbdbd;margin-bottom:7px}
.foot-col.guarantee{left:300px;width:190px}
.foot-col.partners{left:527px;width:190px}
.foot-col.partners strong{display:block;color:#eee;font-size:6px}
.social{display:flex;gap:6px;margin-top:4px}
.social span{width:15px;height:15px;border-radius:50%;background:var(--teal)}
.copyright{position:absolute;top:1166px;left:0;width:753px;height:34px;background:var(--footer-bottom);color:#9a9a9a;font-size:5.5px;text-align:center;line-height:34px}
</style>
</head>
<body>

<header class="site-header">
  <div class="brand"><span class="brand-dot"></span><span class="brand-name">Tane Drain Septic Services</span></div>
  <p class="tagline">Our Septic tank maintenance services will help your septic system perform at optimum efficiency.</p>
  <div class="contact">
    <div class="service">Our Septic tank servicing, installation and parts</div>
    <div class="area">Auckland Wide</div>
    <div class="phone">09 555 0142</div>
    <div class="phone">021 555 0187</div>
  </div>
</header>

<nav class="main-nav">
  <a class="active">HOME</a><a>ABOUT</a><a>DECIPHERING YOUR SEPTIC TANK</a><a>SERVICING &amp; MAINTENANCE</a><a>PARTS</a><a>FREE QUOTE</a><a>CONTACT</a>
</nav>

<section class="hero" role="img" aria-label="Coastal beach photograph with rocky headland and sea">
  <div class="hero-box">
    <h1>WANT TO LEARN MORE ABOUT HOW YOUR SEPTIC TANK WORKS?</h1>
    <p>Tane Drain Septic Services are Auckland's best septic tank experts and will tell you everything there is to know.</p>
  </div>
  <div class="hero-btn">FREE QUOTE</div>
  <div class="hero-arrow left"></div>
  <div class="hero-arrow right"></div>
</section>

<section class="features">
  <article class="feature">
    <h2>Looking for septic tank parts in Auckland ASAP?</h2>
    <div class="feature-img" role="img" aria-label="Photo of septic tank parts on a lawn"></div>
    <p>If you need replacement parts for your septic tank, call us today. Our team will source the right part quickly and can install it for you. We carry lids, filters, pumps and risers for most systems, so your tank keeps working without long delays.</p>
    <span class="more">MORE INFO</span>
  </article>
  <article class="feature">
    <h2>Want to know how to take care of your septic tank?</h2>
    <div class="feature-img" role="img" aria-label="Photo of a septic tank lid in a garden"></div>
    <p>Most people who own a rural property never think about the tank until something goes wrong. A little regular care saves money. Our guide explains what can go down the drain, how often to pump and the warning signs to watch for around your system.</p>
    <span class="more">MORE INFO</span>
  </article>
  <article class="feature">
    <h2>When was the last time you serviced your septic tank?</h2>
    <div class="feature-img" role="img" aria-label="Photo of an open septic tank being serviced"></div>
    <p>Standard septic tanks need to be serviced every three to five years. Skipping a service can lead to blocked pipes, smells and costly repairs. Book a routine check with our friendly team and we will inspect, pump and report on the health of your tank.</p>
    <span class="more">MORE INFO</span>
  </article>
</section>

<section class="wrap quote">
  <h2>FREE QUOTE</h2>
  <p class="sub">Contact you within four hours</p>
  <div class="quote-row">
    <div class="field">Name</div><div class="field">E-mail</div><div class="field">Phone</div>
  </div>
  <div class="field details">Details</div>
  <span class="submit">SUBMIT</span>
</section>

<footer class="site-footer">
  <ul class="foot-links">
    <li>Home</li><li>About</li><li>Deciphering Your Septic tank</li><li>Servicing &amp; Maintenance</li><li>Parts</li><li>Free Quote</li><li>Contact</li>
  </ul>
  <div class="foot-col guarantee">
    <h3>Company guarantee to you</h3>
    <p>Tane Drain Septic Services has worked across the Auckland region for many years. Every job is done by trained staff using modern equipment and careful methods.</p>
    <p>We stand behind our work. If something is not right after a service, we will come back and fix it at no extra cost.</p>
    <p>Call us for honest advice and a clear quote before any work begins.</p>
  </div>
  <div class="foot-col partners">
    <h3>Need your septic tank cleaned?</h3>
    <p>Talk to the team at<strong>Kowhai Tank Cleaning Services</strong></p>
    <h3>Our all polymer fabricated products</h3>
    <p>Talk to the team at<strong>Harbour Lid Limited</strong></p>
    <div class="social"><span></span><span></span><span></span></div>
  </div>
</footer>
<div class="copyright">Copyright © 2014 Tane Drain Septic System . All rights reserved.</div>

</body>
</html>
```